AMBER AND STONE WEB

We need a home design in wordpress, we have now a web but we would like to improve it. Our current web is www.amberandstonevillas.example Our business is holliday rental of villas in Ibiza. Our guest must know that we are a reliable company, professional and with experience and good reviews. We want them to click in our reservation engine: https://bookings.amberandstonevillas.example/en/ and make reservation in our website. We would also like to say that all the properties that we have are just us who commercialize so we have best price available. Many people are going to see our villas in staylister.example and look to our website to make a reservation with us so we need to show them that they are at the right place and click at our link to our reservation engine. What make us special is that we are a local company, we are from Ibiza, Our guests are always received in person by the Amber and Stone Villas team. You will enjoy extensive tourist information when you check in and during the entire stay. You will be attended by ChatLoop and calls, always happy to help so that you have a happy and fun stay! Our guest stay is better than in hotel as they have more spece, private swiming pool, private garden, barbeque ... To rent a villa is the best way to stay in Ibiza. We also have a promotional video: https://vidshare.example/Qm7tLp2Xz9A Let our philosophy be shown, we think that coming on holiday to Ibiza implies seeing the nature that we have in Ibiza, hence our name AMBER AND STONE, like the pins that almost touch the sea in Ibiza, or the posidonea meadows where the intense green of the seaweed and the blue of the sea. We are aware of the environment, and we love Ibiza. For us, the client who visits Ibiza, should rent a car, go around the island, eat in a restaurant one day in front of the sea, is a night of partying to the discs, go shopping, visit the ancient heritage of Umanity, make some aquatic sport, enjoy the pool, those are for us Ibiza.

Target Market(s)

Europe, people from Holand, UK, Germany, France, Spain ...

Industry/Entity Type

Tourism

Colors

Designer to choose colors to be used in the design.

Requirements
Must have
• Pictures of Ibiza.
Nice to have
• Our name Amber and Stone Villas is beacuse in Ibiza there is forest that almost touch the watter of the Mediterranean sea, so you can see green of the forest and blue of the sea and the sky. And also beacause under the watter of the sea there is a plant called Posidonia that is also green please see the picture of posidonia.

```html
<!DOCTYPE html>
<html lang="en">
<head>
<meta charset="utf-8">
<title>Amber and Stone Villas – Home</title>
<link href="https://fonts.googleapis.com/css2?family=Lato:wght@300;400;700;900&display=swap" rel="stylesheet">
<style>
:root{
  --green:#7f9b34;
  --green-head:#87a33b;
  --green-light:#cbd6a8;
  --blue:#2c7df7;
  --grey-nav:#f2f2f2;
  --text:#333;
  --muted:#666;
  --border:#d6d6d6;
}
*{margin:0;padding:0;box-sizing:border-box}
html,body{width:1200px;height:2917px;overflow:hidden}
body{position:relative;font-family:'Lato',sans-serif;color:var(--text);background:#fff}
.abs{position:absolute}
a{color:inherit;text-decoration:none}

.topbar{left:0;top:0;width:1200px;height:37px;background:var(--green);color:#fff;font-size:13px}
.topbar .mail{left:100px;top:10px;display:flex;gap:8px;align-items:center}
.topbar .phone{left:966px;top:10px;display:flex;gap:6px;align-items:center}

.nav{left:0;top:37px;width:1200px;height:80px;background:var(--grey-nav)}
.brand{display:flex;align-items:center;gap:8px;color:var(--green);font-size:16px;letter-spacing:.5px;white-space:nowrap}
.brand .dot{width:18px;height:18px;border-radius:50%;background:var(--green)}
.nav .brand{left:100px;top:30px}
.menu{left:566px;top:29px;display:flex;gap:29px;font-size:15px;color:#8a8a8a;text-transform:uppercase;white-space:nowrap}
.menu a.active{color:var(--green);border-bottom:2px solid var(--green);padding-bottom:5px}

.hero{left:0;top:117px;width:1200px;height:458px;background:linear-gradient(160deg,#2b3c4a 0%,#3f5560 35%,#5a6b4f 65%,#3a4a52 100%)}
.hero h1{left:100px;top:140px;font-size:38px;font-weight:400;color:#fff;white-space:nowrap}
.hero p{left:100px;top:193px;width:430px;font-size:14.5px;line-height:20px;color:#fff}
.btn{display:flex;align-items:center;justify-content:center;gap:8px;border-radius:24px;color:#fff;font-weight:900;font-size:16px;letter-spacing:.3px}
.btn-green{left:100px;top:297px;width:175px;height:46px;background:var(--green)}
.btn-blue{left:333px;top:297px;width:174px;height:46px;background:var(--blue)}
.video{left:617px;top:200px;width:482px;height:400px;background:linear-gradient(180deg,#8fb3c9 0%,#5fa7a4 40%,#3fb1ad 60%,#5c8a4a 85%,#4a7040 100%);box-shadow:0 6px 14px rgba(0,0,0,.25)}
.video svg{position:absolute;left:216px;top:175px}

.booking{left:175px;top:686px;width:833px;height:66px;background:#fff;box-shadow:0 2px 12px rgba(0,0,0,.18)}
.field{top:7px;height:51px;width:182px;border:1px solid var(--border);display:flex;align-items:center;gap:14px;padding-left:10px;color:#a4a88c;font-size:14px;white-space:nowrap}
.book-btn{left:654px;top:7px;width:167px;height:51px;background:var(--blue);color:#fff;font-size:23px;display:flex;align-items:center;justify-content:center;box-shadow:0 2px 6px rgba(0,0,0,.2)}

.sec-title{color:var(--green-head);font-size:28px;font-weight:400;text-transform:uppercase;white-space:nowrap}
.about-title{right:100px;top:866px}
.about-frame{left:513px;top:915px;width:586px;height:493px;border:2px solid var(--blue)}
.about-photo{left:100px;top:993px;width:508px;height:336px;background:linear-gradient(135deg,#4e6a2c 0%,#6e8a3a 45%,#8aa7c9 70%,#5d4e3c 100%);box-shadow:0 3px 8px rgba(0,0,0,.2)}
.about-text{left:636px;top:957px;width:440px;font-size:18px;line-height:27.5px;color:#444}
.about-text p+p{margin-top:27px}
.person-name{left:100px;top:1342px;font-size:29px;font-weight:400;color:#333;white-space:nowrap}
.person-role{left:100px;top:1375px;font-size:20px;color:var(--blue);white-space:nowrap}
.read-more{left:941px;top:1353px;font-size:21px;color:var(--blue);text-decoration:underline}
.dots{left:576px;top:1455px;display:flex;gap:12px;align-items:center}
.dots span{width:14px;height:14px;border-radius:50%;background:var(--green-head)}
.dots span.on{width:18px;height:18px;border:2px solid var(--green-head);box-shadow:inset 0 0 0 3px #fff;background-color:var(--green-head)}

.villas-title{left:0;width:1232px;text-align:center;top:1580px}
.card{width:233px;height:266px;background:#fff;box-shadow:0 2px 10px rgba(0,0,0,.18);border-radius:3px;overflow:hidden}
.card .img{height:209px;position:relative}
.card .img svg{position:absolute;left:98px;top:88px}
.card .name{position:absolute;left:8px;top:215px;font-size:16px;color:#222;white-space:nowrap}
.card .place{position:absolute;left:8px;top:236px;font-size:17px;color:var(--green-head);display:flex;align-items:center;gap:4px;white-space:nowrap}
.card .mini-btn{position:absolute;right:8px;top:242px;width:54px;height:14px;border-radius:7px;background:var(--blue);color:#fff;font-size:6px;font-weight:700;display:flex;align-items:center;justify-content:center}
.img-warm{background:linear-gradient(160deg,#b7743f 0%,#e9dfd2 40%,#c4a48a 70%,#8c6a4a 100%)}
.img-pool{background:linear-gradient(180deg,#7fa7c6 0%,#6d9a6e 45%,#3fa7b7 65%,#2d8fa6 100%)}
.img-tint{background:linear-gradient(160deg,#b7b35a 0%,#d7e0b0 40%,#a9b872 70%,#8b9a56 100%)}

.guests-title{left:0;width:1200px;text-align:center;top:2124px}
.guest{width:345px;height:200px}
.guest .photo{position:absolute;left:0;top:0;width:92px;height:82px}
.guest .gname{position:absolute;left:117px;top:40px;font-size:27px;color:#333;white-space:nowrap}
.guest .gfrom{position:absolute;left:117px;top:73px;font-size:19px;color:var(--blue);white-space:nowrap}
.guest .rule{position:absolute;left:0;top:99px;width:341px;height:2px;background:#cfcfcf}
.guest p{position:absolute;left:0;top:113px;width:345px;font-size:12.8px;line-height:20px;color:#666}

.footer-line{left:0;top:2698px;width:1200px;height:1px;background:#e3e3e3}
.footer-dot{left:596px;top:2694px;width:8px;height:8px;border-radius:50%;background:var(--green)}
.f-head{font-size:25px;color:var(--green-head);font-weight:400;text-transform:uppercase;white-space:nowrap}
.f-list{font-size:16px;color:#333;white-space:nowrap}
.social{left:608px;top:2760px;display:flex;gap:20px}
.social span{width:38px;height:38px;border-radius:50%}
.subscribe{left:608px;top:2828px;width:212px;height:20px;border:1px solid #b5b5b5;display:flex}
.subscribe .in{flex:1;font-size:12px;color:#8a8a8a;padding:2px 7px}
.subscribe .go{width:42px;background:var(--green);display:flex;align-items:center;justify-content:center}
.bottombar{left:0;top:2883px;width:1200px;height:34px;background:var(--blue);color:#fff;font-size:14px;text-align:center;line-height:34px}
</style>
</head>
<body>

<header>
  <div class="abs topbar">
    <div class="abs mail">
      <svg width="22" height="16" viewBox="0 0 22 16" fill="none" stroke="#fff" stroke-width="1.4"><rect x="1" y="1" width="20" height="14"/><path d="M1 1l10 8 10-8M1 15l7-6M21 15l-7-6"/></svg>
      reservas@amberandstonevillas.example
    </div>
    <div class="abs phone">
      <svg width="24" height="22" viewBox="0 0 24 22" fill="none" stroke="#fff" stroke-width="1.4"><path d="M5 2l4 4-2 3c1 3 4 6 7 7l3-2 4 4-3 3C10 20 3 12 2 5z"/></svg>
      +34 600 123 456
    </div>
  </div>
  <nav class="abs nav">
    <a class="abs brand" href="#"><span class="dot"></span>AMBER AND STONE</a>
    <div class="abs menu">
      <a class="active" href="#">Home</a><a href="#">Experience</a><a href="#">All properties</a><a href="#">About us</a><a href="#">Contact us</a>
    </div>
  </nav>
</header>

<section class="abs hero" role="img" aria-label="Photo of a villa garden with palm trees and a pool at dusk in Ibiza">
  <h1 class="abs">The best way to stay in Ibiza!</h1>
  <p class="abs">Lorem ipsum dolor sit amet, consectetur adipiscing elit, sed do eiusmod tempor incididunt ut labore et dolore magna aliqua. Quis ipsum suspendisse ultrices gravida. Risus commodo viverra maecenas accumsan lacus vel facilisis.</p>
  <a class="abs btn btn-green" href="#">BOOK NOW
    <svg width="24" height="24" viewBox="0 0 24 24" fill="none" stroke="#fff" stroke-width="1.6"><circle cx="12" cy="12" r="10.5"/><path d="M7 12h10M13 8l4 4-4 4"/></svg></a>
  <a class="abs btn btn-blue" href="#">ALL PROPERTIES</a>
</section>
<div class="abs video" role="img" aria-label="Promotional video still of a turquoise Ibiza cove with pine forest">
  <svg width="52" height="52" viewBox="0 0 52 52" fill="none" stroke="#1d2a2a" stroke-width="2"><circle cx="26" cy="26" r="24"/><path d="M20 15l15 11-15 11z"/></svg>
</div>

<form class="abs booking">
  <div class="abs field" style="left:13px">
    <svg width="34" height="34" viewBox="0 0 34 34" fill="none" stroke="#b7bd8c" stroke-width="1.5"><rect x="2" y="5" width="30" height="27"/><path d="M2 11h30M9 2v6M25 2v6M8 16h4M15 16h4M22 16h4M8 21h4M15 21h4M22 21h4M8 26h4M15 26h4"/></svg>
    Choose Checkin
  </div>
  <div class="abs field" style="left:227px">
    <svg width="34" height="34" viewBox="0 0 34 34" fill="none" stroke="#b7bd8c" stroke-width="1.5"><rect x="2" y="5" width="30" height="27"/><path d="M2 11h30M9 2v6M25 2v6M8 16h4M15 16h4M22 16h4M8 21h4M15 21h4M22 21h4M8 26h4M15 26h4"/></svg>
    Choose Checkout
  </div>
  <div class="abs field" style="left:440px">
    <svg width="30" height="34" viewBox="0 0 30 34" fill="#a9ae8a"><circle cx="15" cy="10" r="8"/><path d="M1 34c0-10 6-14 14-14s14 4 14 14z"/></svg>
    Adults/Kids
    <svg width="16" height="20" viewBox="0 0 16 20" fill="none" stroke="#b7bd8c" stroke-width="1.3"><path d="M8 1l7 9-7 9-7-9z"/></svg>
  </div>
  <a class="abs book-btn" href="#">BOOK</a>
</form>

<section>
  <h2 class="abs sec-title about-title">Ibiza countryside lovers? So we are</h2>
  <div class="abs about-frame"></div>
  <div class="abs about-photo" role="img" aria-label="Portrait of the general manager seated in a garden"></div>
  <div class="abs about-text">
    <p>I studied Economics and Business Administration at the University of Valdora (Spain) and at the Hollandsberg University in Ghent (Belgium), after working for 7 years as a manager of a well-known luxury hotel in Ibiza, I decided to found Amber and Stone Villas.</p>
    <p>I consider myself an admirer of the houses on the countryside of Ibiza. I spent my childhood in Cala Portinax (Ibiza), my parents had a house with a garden with sea view. I firmly believe that coming to Ibiza and staying in a house is undoubtedly the best option to spend your holiday.</p>
  </div>
  <div class="abs person-name">MARCO FERRER</div>
  <div class="abs person-role">General Manager</div>
  <a class="abs read-more" href="#">READ MORE</a>
  <div class="abs dots"><span class="on"></span><span></span></div>
</section>

<svg class="abs" style="left:0;top:1580px" width="1200" height="1100" viewBox="0 1580 1200 1100">
  <path d="M1200 1590 C1000 1650 830 1790 790 1985 C900 2090 1070 2200 1200 2265 Z" fill="var(--blue)"/>
  <circle cx="-147" cy="2287" r="283" fill="none" stroke="var(--green-light)" stroke-width="80"/>
</svg>

<section>
  <h2 class="abs sec-title villas-title">Our villa's</h2>
  <svg class="abs" style="left:76px;top:1810px" width="20" height="36" viewBox="0 0 20 36" fill="none" stroke="#333" stroke-width="1.8"><path d="M18 2L2 18l16 16"/></svg>

  <article class="abs card" style="left:175px;top:1699px">
    <div class="img img-warm" role="img" aria-label="Interior of a rustic farmhouse living room">
      <svg width="38" height="34" viewBox="0 0 38 34" fill="none" stroke="#333" stroke-width="1.6"><rect x="7" y="2" width="29" height="22"/><rect x="2" y="8" width="29" height="24" fill="rgba(255,255,255,.35)"/><circle cx="16" cy="17" r="3"/><path d="M4 30l9-8 6 5 5-4 7 7"/></svg>
    </div>
    <div class="name">Agroturismo Can Roure</div>
    <div class="place"><svg width="10" height="14" viewBox="0 0 10 14" fill="#222"><path d="M5 0a5 5 0 015 5c0 4-5 9-5 9S0 9 0 5a5 5 0 015-5zm0 3a2 2 0 100 4 2 2 0 000-4z"/></svg>san carlos</div>
    <a class="mini-btn" href="#">BOOK NOW</a>
  </article>

  <article class="abs card" style="left:468px;top:1698px">
    <div class="img img-pool" role="img" aria-label="Villa swimming pool with garden and white house">
      <svg width="38" height="34" viewBox="0 0 38 34" fill="none" stroke="#333" stroke-width="1.6"><rect x="7" y="2" width="29" height="22"/><rect x="2" y="8" width="29" height="24" fill="rgba(255,255,255,.35)"/><circle cx="16" cy="17" r="3"/><path d="M4 30l9-8 6 5 5-4 7 7"/></svg>
    </div>
    <div class="name">Villa Can Lluna</div>
    <div class="place"><svg width="10" height="14" viewBox="0 0 10 14" fill="#222"><path d="M5 0a5 5 0 015 5c0 4-5 9-5 9S0 9 0 5a5 5 0 015-5zm0 3a2 2 0 100 4 2 2 0 000-4z"/></svg>Saint Joseph</div>
    <a class="mini-btn" href="#">BOOK NOW</a>
  </article>

  <article class="abs card" style="left:747px;top:1693px">
    <div class="img img-tint" role="img" aria-label="Interior of a villa living room">
      <svg width="38" height="34" viewBox="0 0 38 34" fill="none" stroke="#333" stroke-width="1.6"><rect x="7" y="2" width="29" height="22"/><rect x="2" y="8" width="29" height="24" fill="rgba(255,255,255,.35)"/><circle cx="16" cy="17" r="3"/><path d="M4 30l9-8 6 5 5-4 7 7"/></svg>
    </div>
    <div class="name">Villa Las Dos Palmas</div>
    <div class="place"><svg width="10" height="14" viewBox="0 0 10 14" fill="#222"><path d="M5 0a5 5 0 015 5c0 4-5 9-5 9S0 9 0 5a5 5 0 015-5zm0 3a2 2 0 100 4 2 2 0 000-4z"/></svg>San Antonio</div>
    <a class="mini-btn" href="#">BOOK NOW</a>
  </article>

  <article class="abs card" style="left:1027px;top:1696px">
    <div class="img img-tint" role="img" aria-label="Interior of a villa living room">
      <svg width="38" height="34" viewBox="0 0 38 34" fill="none" stroke="#333" stroke-width="1.6"><rect x="7" y="2" width="29" height="22"/><rect x="2" y="8" width="29" height="24" fill="rgba(255,255,255,.35)"/><circle cx="16" cy="17" r="3"/><path d="M4 30l9-8 6 5 5-4 7 7"/></svg>
    </div>
    <div class="name">Villa Can Sorell Mar</div>
    <div class="place"><svg width="10" height="14" viewBox="0 0 10 14" fill="#222"><path d="M5 0a5 5 0 015 5c0 4-5 9-5 9S0 9 0 5a5 5 0 015-5zm0 3a2 2 0 100 4 2 2 0 000-4z"/></svg>Ibiza Town</div>
    <a class="mini-btn" href="#">BOOK NOW</a>
  </article>
</section>

<section>
  <h2 class="abs sec-title guests-title">Our guests experience</h2>

  <article class="abs guest" style="left:191px;top:2218px">
    <div class="photo" style="background:linear-gradient(135deg,#cfd6dc,#8a7a6c)" role="img" aria-label="Guest portrait"></div>
    <div class="gname">Mike</div><div class="gfrom">United Kingdom</div><div class="rule"></div>
    <p>Lorem ipsum dolor sit amet, consectetur adipiscing elit, sed do eiusmod tempor incididunt ut labore et dolore magna aliqua. Quis ipsum suspendisse ultrices gravida. Risus commodo viverra maecenas accumsan lacus vel facilisis.</p>
  </article>
  <article class="abs guest" style="left:675px;top:2220px">
    <div class="photo" style="background:linear-gradient(135deg,#3c3a36,#8a5a44)" role="img" aria-label="Guest portrait"></div>
    <div class="gname" style="left:115px">William</div><div class="gfrom" style="left:115px">United States</div><div class="rule"></div>
    <p>Lorem ipsum dolor sit amet, consectetur adipiscing elit, sed do eiusmod tempor incididunt ut labore et dolore magna aliqua. Quis ipsum suspendisse ultrices gravida. Risus commodo viverra maecenas accumsan lacus vel facilisis.</p>
  </article>
  <article class="abs guest" style="left:191px;top:2449px">
    <div class="photo" style="background:linear-gradient(135deg,#c9ced2,#6d7480)" role="img" aria-label="Guest portrait"></div>
    <div class="gname">Max</div><div class="gfrom">Europe</div><div class="rule"></div>
    <p>Lorem ipsum dolor sit amet, consectetur adipiscing elit, sed do eiusmod tempor incididunt ut labore et dolore magna aliqua. Quis ipsum suspendisse ultrices gravida. Risus commodo viverra maecenas accumsan lacus vel facilisis.</p>
  </article>
  <article class="abs guest" style="left:675px;top:2449px">
    <div class="photo" style="background:linear-gradient(135deg,#c8a07a,#8e9fb4)" role="img" aria-label="Guest portrait"></div>
    <div class="gname" style="left:116px">Pricy</div><div class="gfrom" style="left:116px">United Kingtom</div><div class="rule"></div>
    <p>Lorem ipsum dolor sit amet, consectetur adipiscing elit, sed do eiusmod tempor incididunt ut labore et dolore magna aliqua. Quis ipsum suspendisse ultrices gravida. Risus commodo viverra maecenas accumsan lacus vel facilisis.</p>
  </article>
</section>

<footer>
  <div class="abs footer-line"></div>
  <div class="abs footer-dot"></div>

  <h3 class="abs f-head" style="left:99px;top:2715px">Contact</h3>
  <address class="abs f-list" style="left:100px;top:2751px;font-style:normal;line-height:25px">
    Amber &amp; Stone Villas<br>Calle de los Almendros<br>3, Sant Miquel de Balansat,<br>07815, Ibiza<br>Spain.
  </address>

  <h3 class="abs f-head" style="left:340px;top:2715px">Helpful</h3>
  <ul class="abs f-list" style="left:342px;top:2743px;list-style:none;line-height:23.4px">
    <li>Home</li><li>Experiences</li><li>About us</li><li>Contact us</li><li>All properties</li><li>Book</li>
  </ul>

  <h3 class="abs f-head" style="left:607px;top:2715px">Connect with us</h3>
  <div class="abs social">
    <span style="background:#3b5a9a"></span><span style="background:#2d9fe0"></span><span style="background:#c0392b"></span><span style="background:#dd4b39"></span>
  </div>
  <div class="abs subscribe">
    <span class="in">SUBSCRIBE</span>
    <span class="go"><svg width="18" height="12" viewBox="0 0 18 12" fill="none" stroke="#fff" stroke-width="1.2"><rect x="1" y="1" width="16" height="10"/><path d="M1 1l8 6 8-6"/></svg></span>
  </div>

  <div class="abs brand" style="left:925px;top:2788px"><span class="dot"></span>AMBER AND STONE</div>

  <div class="abs bottombar">©2019&nbsp;&nbsp; All rights reserved to Amber &amp; Stone Villas</div>
</footer>

</body>
</html>
```